New Business Card for Innovative Tool Company

We need a new design of business card for our florida based tool manufacturing company. I will attach 2 files that we use for our logo, use whichever you feel works best for the card. Main colours are as per logo, and we can use different shades of black/white/grey for the background.

Contact Information for Business Card

Name/Jobtitle/cell
Corvalen Tools
Suite 212c
4316 Marrowdale Pkw
Orlando, FL32847
USA
name@corvaleninc.example
www.corvaleninc.example

Font styles to use
Sans Serif

Colors

Designer to choose colors to be used in the design.

Requirements
Must have
• Icons for Plazaro, Chirpet, Snapvale, Findlo & Vidstream

```html
<!DOCTYPE html>
<html lang="en">
<head>
<meta charset="utf-8">
<title>Corvalen Tools – Business Card</title>
<link rel="stylesheet" href="https://fonts.googleapis.com/css2?family=Roboto:wght@400;500;700;900&display=swap">
<style>
  :root {
    --stage: #2b2b2b;
    --stage-light: #4a4a4a;
    --card: #545454;
    --card-deep: #3e3e3e;
    --accent: #fcee3a;
    --ink: #ffffff;
    --faint: #4c4c4c;
    --faint-line: #474747;
  }
  * { box-sizing: border-box; margin: 0; padding: 0; }
  html, body { width: 1200px; height: 1000px; overflow: hidden; }
  body {
    background: radial-gradient(ellipse at 50% 35%, var(--stage-light), var(--stage) 75%);
    font-family: "Roboto", Arial, sans-serif;
    position: relative;
  }
  .card {
    position: absolute;
    left: 250px;
    width: 700px;
    height: 400px;
    border-radius: 26px;
    background: var(--card);
    overflow: hidden;
    box-shadow: 0 18px 40px rgba(0,0,0,.45);
  }
  .card--back { top: 60px; }
  .card--front { top: 530px; }

  /* back */
  .back-decor {
    position: absolute; left: -70px; top: -60px;
    width: 420px; height: 420px; border-radius: 50%;
    border: 2px solid var(--faint-line);
    display: flex; align-items: center; justify-content: center;
  }
  .back-decor__name {
    font-size: 58px; font-weight: 900; color: var(--faint);
    text-transform: uppercase; line-height: 1; text-align: center;
  }
  .brand {
    position: absolute; right: 40px; bottom: 48px;
    display: flex; flex-direction: column; align-items: center; gap: 14px;
  }
  .brand__circle {
    width: 92px; height: 92px; border-radius: 50%;
    border: 2px solid var(--accent);
  }
  .brand__name {
    font-size: 34px; font-weight: 900; color: var(--accent);
    text-transform: uppercase; letter-spacing: .5px;
  }

  /* front */
  .front-mark {
    position: absolute; left: 40px; top: 70px;
    width: 200px; height: 200px; border-radius: 50%;
    border: 2px solid var(--accent);
    display: flex; align-items: center; justify-content: center;
  }
  .front-mark__name {
    font-size: 26px; font-weight: 900; color: var(--accent);
    text-transform: uppercase; text-align: center; line-height: 1.1;
  }
  .divider {
    position: absolute; left: 268px; top: 50px;
    width: 4px; height: 250px; background: var(--accent);
  }
  .contact {
    position: absolute; left: 298px; top: 48px; color: var(--ink);
  }
  .contact__name {
    font-size: 24px; font-weight: 700; color: var(--accent);
    text-transform: uppercase;
  }
  .contact__title { font-size: 17px; margin-top: 2px; }
  .contact__address { font-size: 17px; line-height: 1.25; margin-top: 16px; }
  .contact__line {
    display: flex; align-items: center; gap: 8px;
    font-size: 17px; margin-top: 6px;
  }
  .contact__line svg { flex: none; }
  .social {
    display: flex; gap: 12px; margin-top: 14px; list-style: none;
  }
  .social__item {
    display: flex; align-items: center; gap: 4px;
    font-size: 12px; font-weight: 500; color: var(--accent);
  }
  .social__dot {
    width: 12px; height: 12px; border-radius: 50%; background: var(--accent);
  }
  .wave { position: absolute; left: 0; bottom: 0; }
</style>
</head>
<body>

<section class="card card--back" aria-label="Card back">
  <div class="back-decor"><span class="back-decor__name">Corvalen<br>Tools</span></div>
  <div class="brand">
    <span class="brand__circle"></span>
    <span class="brand__name">Corvalen Tools</span>
  </div>
</section>

<section class="card card--front" aria-label="Card front">
  <svg class="wave" width="700" height="400" viewBox="0 0 700 400" aria-hidden="true">
    <path d="M0 280 C 130 300, 260 360, 420 330 C 540 305, 620 250, 700 240 L700 400 L0 400 Z" fill="var(--card-deep)"/>
    <path d="M0 300 C 130 320, 270 380, 430 350 C 550 325, 630 275, 700 268 L700 400 L0 400 Z" fill="var(--accent)"/>
  </svg>

  <div class="front-mark"><span class="front-mark__name">Corvalen<br>Tools</span></div>
  <div class="divider"></div>

  <div class="contact">
    <p class="contact__name">Marlon Feske</p>
    <p class="contact__title">Managing Director</p>
    <p class="contact__address">Suite 212c 4316 Marrowdale<br>Pkw Orlando, FL32847 USA</p>
    <p class="contact__line">
      <svg width="14" height="11" viewBox="0 0 14 11"><rect width="14" height="11" rx="1.5" fill="var(--accent)"/><path d="M1 1.5 7 6 13 1.5" stroke="var(--card)" stroke-width="1.4" fill="none"/></svg>
      name@corvaleninc.example
    </p>
    <p class="contact__line">
      <svg width="14" height="14" viewBox="0 0 14 14"><circle cx="7" cy="7" r="7" fill="var(--accent)"/><path d="M0.5 7h13M7 0.5c-3 3-3 10 0 13M7 0.5c3 3 3 10 0 13" stroke="var(--card)" stroke-width="1" fill="none"/></svg>
      www.corvaleninc.example
    </p>
    <ul class="social">
      <li class="social__item"><span class="social__dot"></span>Plazaro</li>
      <li class="social__item"><span class="social__dot"></span>Chirpet</li>
      <li class="social__item"><span class="social__dot"></span>Vidstream</li>
      <li class="social__item"><span class="social__dot"></span>Findlo</li>
      <li class="social__item"><span class="social__dot"></span>Snapvale</li>
    </ul>
  </div>
</section>

</body>
</html>
```